Digitalization Training Site - Koru Theme (mandatory)

Hi,
I have a Koru theme website running on Wordpress and I need a design.

Designs must be possible with standard Koru theme and minimal/no CSS customization or similar. if this is required please note this in submission. Also, please note mobile and device usage which must be universal.

Koru Theme:
https://www.brightlanestudio.example

Target Market: education, online training, IT training, digitalization, digital transformation, disruption

Target Group: IT students, IT Management students, IT companies showing examples, IT companies recruiting, lectures, trainers, training companies

Look and Feel:
- Elegant, Playful, Fresh, Plain, Personable, Economical

Main Colors:
- Background: mainly white/light grey (like logo), a few parts maybe in orange (like the logo colors)
- design elements: logo colors (grey, dark yellow – orange, and one extra color: a darker blue that fits to the logo colors)
- text: grey, black, white - depending on background, good readable

Form
- round buttons
- full with
- responsive for desktop, tablet and mobile (koru is supporting this ;)
- animation like on the Koru layout for e-courses (see below)

I have attached:
- logo files (ai, png, jpg, eps)
- some design parts that I like (samples for blocks)

To be delivered:
- koru layout (zipped json files)
- all pictures, icons, and illustrations (high res. : ai, psd, eps, jpg, png)

There is a Koru Layout for e-courses that is partly interesting you can find it here:
- https://www.brightlanestudio.example/blog/koru-resources/download-a-free-breathtaking-learning-management-lms-layout-pack-for-koru
- Can be used as idea for building blocks

I need at least 20 building blocks (see examples I uploaded) for homepage, landing page, shop, product page, marketing, landing, about us, etc. The building blocks could be
- Slider (for home page) (I like the light bulbs in one of the examples)
- Content blocks with illustrations
- Get started area (free & premium)
- Choose a plan
- Our Process (5-6 steps)
- Woocommerce shop page
- Woocommerce product page
- We offer
- Footer
I like the footer animation in this example: http://demo.korumodules.example/koru-edu//gallery/
- Contact
- see Koru Layout example for more Blocks
NOT:
- Newsletter

Best regards
Marten

Target Market(s)

Industry/Entity Type

Training

Coding

Coded - Design and coding required

Number of Pages Required

5+ page

Font styles to use
Serif

Colors
ffcf3e
ffc214
faa54b
f78f20
f68e4e
f37122
3276b5
99b9da
959595

Requirements
Must have
• Designs must be possible with standard Koru theme and minimal/no CSS customization or similar. if this is required please note this in submission. Also, please note mobile and device usage which must be universal.
• adopt design preference (logo colors etc. - see big text)
• To be delivered:
• - koru layout (zipped json files)
• - all pictures, icons, and illustrations (high res. : ai, psd, eps, jpg, png)
Nice to have
• Ideas for good design for a online-course site

```html
<!DOCTYPE html>
<html lang="en">
<head>
<meta charset="utf-8">
<title>Institute of Digital Craft</title>
<link href="https://fonts.googleapis.com/css2?family=Montserrat:wght@400;600;700&family=Open+Sans:wght@400;600;700&display=swap" rel="stylesheet">
<style>
:root{
  --orange:#f37122;
  --orange-soft:#f78f20;
  --amber:#ffc214;
  --yellow:#ffcf3e;
  --blue:#3276b5;
  --blue-light:#99b9da;
  --grey:#959595;
  --grey-dark:#5a5a5a;
  --ink:#222;
  --light:#f4f4f4;
  --footer:#161616;
  --footer-bar:#0b0b0b;
}
*{margin:0;padding:0;box-sizing:border-box}
html,body{width:1200px;height:4615px;overflow:hidden}
body{position:relative;background:#fff;font-family:"Open Sans",Arial,sans-serif;color:var(--grey-dark)}
.abs{position:absolute}
section,header,footer{position:absolute;left:0;width:1200px;overflow:hidden}
h2.section-title{position:absolute;left:0;width:1200px;text-align:center;font-family:"Montserrat",Arial,sans-serif;font-weight:700;font-size:40px;color:var(--ink)}
.title-rule{position:absolute;left:280px;width:640px;height:1px;background:#ddd}
.title-rule::after{content:"";position:absolute;left:316px;top:-3px;width:8px;height:7px;background:var(--orange)}
.btn{position:absolute;display:flex;align-items:center;justify-content:center;border-radius:24px;font-family:"Montserrat",Arial,sans-serif;font-weight:600;font-size:14px;letter-spacing:.5px;text-transform:uppercase}

/* header */
.site-header{top:0;height:110px;background:#fff;border-top:4px solid var(--orange);box-shadow:0 2px 6px rgba(0,0,0,.08);z-index:2}
.brand{left:96px;top:24px;display:flex;align-items:center;gap:14px}
.brand-mark{width:52px;height:52px;background:var(--orange);border-radius:6px}
.brand-name{font-family:"Montserrat",Arial,sans-serif;font-weight:600;font-size:22px;line-height:26px;color:var(--grey-dark);width:190px}
.main-nav{left:415px;top:0;height:106px;display:flex;align-items:center;font-family:"Montserrat",Arial,sans-serif;font-size:16px;color:var(--grey-dark)}
.main-nav a{display:flex;align-items:center;height:106px;padding:0 22px;color:inherit;text-decoration:none}
.main-nav a.active{background:var(--orange);color:#fff;padding:0 26px;margin-right:38px}
.main-nav .search{margin-left:20px}

/* hero */
.hero{top:110px;height:490px}
.hero-photo{position:absolute;inset:0;background:linear-gradient(100deg,#8c7d74 0%,#b3a8a0 35%,#d9d2cc 60%,#7d6f66 100%)}
.hero-shade{position:absolute;inset:0;background:linear-gradient(90deg,rgba(0,0,0,.45),rgba(0,0,0,0) 55%)}
.hero h1{position:absolute;left:100px;top:135px;font-family:"Montserrat",Arial,sans-serif;font-weight:700;font-size:42px;color:#fff}
.hero p{position:absolute;left:100px;top:196px;font-size:20px;color:#fff;letter-spacing:.5px}
.hero .btn{left:100px;top:260px;width:160px;height:44px;border:2px solid #fff;color:#fff}
.slider-dots{position:absolute;left:100px;top:334px;display:flex;gap:8px}
.slider-dots span{width:12px;height:12px;border-radius:50%;border:2px solid #fff}
.slider-dots span.on{background:var(--orange);border-color:var(--orange)}

/* about */
.about{top:600px;height:477px;border-bottom:1px solid #eee}
.about-mark{position:absolute;left:92px;top:140px;width:340px;height:190px;display:flex;align-items:center;font-family:"Montserrat",Arial,sans-serif;font-weight:700;font-size:60px;line-height:62px;color:var(--grey)}
.about-divider{position:absolute;left:466px;top:82px;width:1px;height:300px;background:#ddd}
.about h2{position:absolute;left:498px;top:82px;font-family:"Montserrat",Arial,sans-serif;font-weight:700;font-size:38px;color:var(--ink)}
.about .accent{position:absolute;left:498px;top:135px;width:9px;height:7px;background:var(--orange)}
.about p{position:absolute;left:498px;top:164px;width:610px;font-size:13px;line-height:22px;color:var(--grey)}
.about .btn{left:498px;top:344px;width:150px;height:40px;background:var(--orange);color:#fff}

/* services */
.services{top:1077px;height:692px;background:linear-gradient(180deg,#eeeeee,#f7f7f7 40%,#e6e6e6)}
.services h2.section-title{top:82px}
.services .title-rule{top:140px}
.service{position:absolute;width:400px}
.service h3{font-family:"Montserrat",Arial,sans-serif;font-weight:600;font-size:19px;color:var(--ink);margin-bottom:6px}
.service p{font-size:13px;line-height:20px;color:var(--grey)}
.service .more{display:inline-block;margin-top:4px;font-size:12px;color:var(--orange)}
.service.left{left:70px;text-align:right}
.service.right{left:728px}
.service-icon{position:absolute;width:100px;height:100px;border-radius:50%;display:flex;align-items:center;justify-content:center}
.service-icon.orange{background:var(--orange)}
.service-icon.grey{background:var(--grey)}

/* process */
.process{top:1769px;height:994px;background:#fff}
.process h2.section-title{top:80px}
.process .title-rule{top:135px}
.process svg.diagram{position:absolute;left:0;top:0}
.step{position:absolute;width:280px;text-align:center}
.step h3{font-family:"Montserrat",Arial,sans-serif;font-weight:600;font-size:18px;color:var(--ink);margin-bottom:8px}
.step p{font-size:13px;line-height:19px;color:var(--grey)}

/* testimonials */
.testimonials{top:2763px;height:498px;background:linear-gradient(180deg,#f1f1f1,#fafafa)}
.testimonials h2.section-title{top:95px}
.testimonials .title-rule{top:152px}
.testimonial{position:absolute;top:210px;width:320px}
.avatar{position:absolute;left:0;top:12px;width:70px;height:70px;border-radius:50%;background:linear-gradient(135deg,#c9b8ad,#8e7e73);border:3px solid #fff;box-shadow:0 1px 4px rgba(0,0,0,.15)}
.quote-mark{position:absolute;left:86px;top:2px;font-family:"Montserrat",Arial,sans-serif;font-size:34px;font-weight:700;color:var(--orange);line-height:1}
.testimonial blockquote{position:absolute;left:110px;top:12px;width:210px;font-size:13px;line-height:19px;color:var(--grey)}
.testimonial .who{position:absolute;left:0;top:96px;font-family:"Montserrat",Arial,sans-serif;font-size:12px;font-weight:600;color:var(--grey-dark);text-transform:uppercase}
.testimonial .role{position:absolute;left:0;top:118px;width:320px;font-size:12px;color:var(--grey);white-space:nowrap}
.stars{position:absolute;left:0;top:150px;display:flex;gap:4px}
.slide-arrow{position:absolute;width:34px;height:34px;border-radius:50%;background:#fff;box-shadow:0 1px 3px rgba(0,0,0,.2);display:flex;align-items:center;justify-content:center}

/* clients */
.clients{top:3261px;height:354px;background:#fff}
.clients h2.section-title{top:84px}
.clients .title-rule{top:140px}
.client-row{position:absolute;left:114px;top:178px;display:flex;gap:1px;background:#e5e5e5;border:1px solid #e5e5e5}
.client{width:161px;height:90px;background:#fff;display:flex;align-items:center;justify-content:center;font-family:"Montserrat",Arial,sans-serif;font-weight:700;font-size:17px;color:#333;gap:8px;white-space:nowrap}
.client i{display:block;width:14px;height:14px;background:#333}
.client-arrow{position:absolute;top:210px;font-size:28px;color:#333;font-family:"Montserrat",Arial,sans-serif}

/* contact */
.contact{top:3615px;height:600px;background:linear-gradient(180deg,var(--orange),#e8661c)}
.contact h2.section-title{top:90px;color:#fff}
.contact .title-rule{top:148px;background:rgba(255,255,255,.5)}
.contact .title-rule::after{background:#fff}
.field{position:absolute;height:46px;background:#fff;font-size:13px;color:#aaa;padding:14px 14px}
.contact .btn{left:409px;top:480px;width:380px;height:46px;border-radius:4px;background:var(--blue);color:#fff}

/* footer */
.site-footer{top:4215px;height:400px;background:var(--footer);color:#ddd}
.footer-brand{left:112px;top:118px;display:flex;align-items:center;gap:12px}
.footer-brand .brand-mark{width:48px;height:48px}
.footer-brand .brand-name{color:#fff;font-size:20px;line-height:24px}
.socials{left:122px;top:196px;display:flex;gap:12px}
.socials span{width:34px;height:34px;border-radius:50%;border:2px solid #fff}
.footer-col h4{font-family:"Montserrat",Arial,sans-serif;font-weight:600;font-size:18px;color:#fff;margin-bottom:18px}
.footer-col li{list-style:none;font-size:13px;line-height:30px;color:#cfcfcf}
.contact-list li{display:flex;gap:14px;align-items:flex-start;line-height:20px;margin-bottom:20px}
.copyright{position:absolute;left:0;top:354px;width:1200px;height:46px;background:var(--footer-bar);color:#ccc;font-size:12px;display:flex;align-items:center;justify-content:center}
</style>
</head>
<body>

<header class="site-header">
  <div class="brand abs"><span class="brand-mark"></span><span class="brand-name">Institute of Digital Craft</span></div>
  <nav class="main-nav abs">
    <a class="active" href="#">Home</a>
    <a href="#">About us</a>
    <a href="#">Services</a>
    <a href="#">Process</a>
    <a href="#">Blog</a>
    <a href="#">Contact us</a>
    <span class="search"><svg width="18" height="18" viewBox="0 0 18 18"><circle cx="7.5" cy="7.5" r="5.5" fill="none" stroke="#f37122" stroke-width="2"/><line x1="11.5" y1="11.5" x2="16" y2="16" stroke="#f37122" stroke-width="2"/></svg></span>
  </nav>
</header>

<section class="hero">
  <div class="hero-photo" role="img" aria-label="Photo of a smiling young professional woman in front of a team meeting in a bright office"></div>
  <div class="hero-shade"></div>
  <h1>Institute of Digital Craft</h1>
  <p>We are a digitalisation training company</p>
  <span class="btn">Read more</span>
  <div class="slider-dots"><span class="on"></span><span></span><span></span><span></span></div>
</section>

<section class="about">
  <div class="about-mark">Digital<br>Craft</div>
  <div class="about-divider"></div>
  <h2>About us</h2>
  <span class="accent"></span>
  <p>We help students, trainers and companies grow their digital skills through practical courses and guided projects. Our team blends teaching experience with real industry work, so every lesson connects theory to daily practice. From first steps in coding to leading a full digital transformation, we build learning paths that fit each learner and each organisation, and we stay beside them as they apply new knowledge at work.</p>
  <span class="btn">Read more</span>
</section>

<section class="services" role="region" aria-label="Our services">
  <div class="abs" style="inset:0;background:linear-gradient(120deg,rgba(255,255,255,.2),rgba(200,200,200,.25))" role="img" aria-label="Faint background photo of hands working at a laptop"></div>
  <h2 class="section-title">Our Services</h2>
  <div class="title-rule"></div>

  <div class="service left" style="top:208px"><h3>Education</h3><p>Structured courses for students who want a strong start in modern digital topics.</p><span class="more">Read More &rsaquo;</span></div>
  <div class="service right" style="top:208px"><h3>Digitalisation</h3><p>We guide teams as they move daily work and processes onto digital tools.</p><span class="more">Read More &rsaquo;</span></div>
  <div class="service left" style="top:350px"><h3>Online training</h3><p>Flexible live and recorded lessons that learners can follow from any place.</p><span class="more">Read More &rsaquo;</span></div>
  <div class="service right" style="top:350px"><h3>Digital transformation</h3><p>Clear plans and coaching for leaders who reshape how their company works.</p><span class="more">Read More &rsaquo;</span></div>
  <div class="service left" style="top:491px"><h3>IT training</h3><p>Hands-on workshops on systems, code and security for technical staff.</p><span class="more">Read More &rsaquo;</span></div>
  <div class="service right" style="top:491px"><h3>Disruption</h3><p>Sessions on new business models and how to respond to fast market change.</p><span class="more">Read More &rsaquo;</span></div>

  <div class="service-icon orange" style="left:488px;top:208px"><svg width="48" height="48" viewBox="0 0 48 48" fill="none" stroke="#fff" stroke-width="2.5"><path d="M4 18 24 9l20 9-20 9z"/><path d="M12 22v10c0 3 6 6 12 6s12-3 12-6V22"/><path d="M44 18v12"/></svg></div>
  <div class="service-icon grey" style="left:612px;top:208px"><svg width="48" height="48" viewBox="0 0 48 48" fill="none" stroke="#fff" stroke-width="2.5"><circle cx="24" cy="24" r="17"/><ellipse cx="24" cy="24" rx="7" ry="17"/><path d="M7 24h34"/></svg></div>
  <div class="service-icon grey" style="left:488px;top:350px"><svg width="48" height="48" viewBox="0 0 48 48" fill="none" stroke="#fff" stroke-width="2.5"><rect x="6" y="9" width="36" height="24" rx="2"/><path d="M18 40h12M24 33v7"/></svg></div>
  <div class="service-icon orange" style="left:612px;top:350px"><svg width="48" height="48" viewBox="0 0 48 48" fill="none" stroke="#fff" stroke-width="2.5"><rect x="11" y="6" width="26" height="36" rx="2"/><rect x="15" y="10" width="18" height="8"/><path d="M16 24h3M23 24h3M30 24h2M16 30h3M23 30h3M30 30h2M16 36h3M23 36h3M30 36h2"/></svg></div>
  <div class="service-icon orange" style="left:488px;top:491px"><svg width="48" height="48" viewBox="0 0 48 48" fill="none" stroke="#fff" stroke-width="2.5"><circle cx="24" cy="24" r="6"/><path d="M24 8v6M24 34v6M8 24h6M34 24h6M12.7 12.7l4.2 4.2M31.1 31.1l4.2 4.2M12.7 35.3l4.2-4.2M31.1 16.9l4.2-4.2"/></svg></div>
  <div class="service-icon grey" style="left:612px;top:491px"><svg width="48" height="48" viewBox="0 0 48 48" fill="#fff"><path d="M27 5 12 27h10l-3 16 17-24H26z"/></svg></div>
</section>

<section class="process">
  <h2 class="section-title">Our Process</h2>
  <div class="title-rule"></div>
  <svg class="diagram" width="1200" height="994" viewBox="0 0 1200 994">
    <circle cx="572" cy="569" r="60" fill="#fff" stroke="#e0e0e0" stroke-width="6"/>
    <circle cx="572" cy="569" r="34" fill="#959595"/>
    <g stroke-width="6" fill="none" stroke-linecap="round">
      <path d="M572 509 V482" stroke="#ffc214"/>
      <path d="M626 547 L660 535" stroke="#f78f20"/>
      <path d="M610 615 L632 650" stroke="#3276b5"/>
      <path d="M534 615 L512 650" stroke="#f37122"/>
      <path d="M516 547 L492 539" stroke="#99b9da"/>
    </g>
    <g fill="#fff" stroke-width="6">
      <circle cx="572" cy="452" r="30" stroke="#ffc214"/>
      <circle cx="692" cy="545" r="30" stroke="#f78f20"/>
      <circle cx="655" cy="683" r="30" stroke="#3276b5"/>
      <circle cx="492" cy="683" r="30" stroke="#f37122"/>
      <circle cx="461" cy="539" r="30" stroke="#99b9da"/>
    </g>
    <g stroke-width="5" stroke-linecap="round" fill="none">
      <path d="M572 422 V380 M563 390 572 378 581 390" stroke="#ffc214"/>
      <path d="M722 535 L762 522 M750 516 764 521 756 534" stroke="#f78f20"/>
      <path d="M676 706 L700 734 M688 734 702 736 702 722" stroke="#3276b5"/>
      <path d="M472 706 L450 734 M446 722 448 736 462 734" stroke="#f37122"/>
      <path d="M431 530 L398 520 M408 512 396 519 404 530" stroke="#99b9da"/>
    </g>
    <g fill="#959595">
      <circle cx="572" cy="452" r="10"/><circle cx="692" cy="545" r="10"/><circle cx="655" cy="683" r="10"/><circle cx="492" cy="683" r="10"/><circle cx="461" cy="539" r="10"/>
    </g>
    <g fill="none" stroke="#ffc214" stroke-width="3"><circle cx="572" cy="216" r="14"/><circle cx="572" cy="216" r="7"/><circle cx="572" cy="216" r="1.5" fill="#ffc214"/></g>
    <path d="M905 417 l5 11 12 1-9 8 3 12-11-6-11 6 3-12-9-8 12-1z" fill="#ffc214"/>
    <path d="M772 716 l14-14 6 6-14 14h-6z" fill="#ffc214"/>
    <g fill="none" stroke="#f78f20" stroke-width="3"><path d="M426 736 a11 11 0 0 1 22 0"/><rect x="422" y="734" width="6" height="10" rx="2" fill="#f78f20"/><rect x="446" y="734" width="6" height="10" rx="2" fill="#f78f20"/></g>
    <g fill="#f78f20"><circle cx="292" cy="482" r="6"/><circle cx="280" cy="486" r="5"/><circle cx="304" cy="486" r="5"/><path d="M282 500a10 8 0 0 1 20 0z"/><path d="M270 502a9 7 0 0 1 14 0zM300 502a9 7 0 0 1 14 0z"/></g>
  </svg>
  <div class="step" style="left:432px;top:244px"><h3>Scoping</h3><p>We map your goals, skills and gaps to agree on a clear training scope.</p></div>
  <div class="step" style="left:765px;top:458px"><h3>Implementation</h3><p>Courses and tools roll out step by step, tuned to each team and role.</p></div>
  <div class="step" style="left:635px;top:752px"><h3>Training</h3><p>Trainers lead practical sessions where learners apply skills on real tasks.</p></div>
  <div class="step" style="left:297px;top:766px"><h3>Support</h3><p>After each course we stay close with coaching, answers and fresh material.</p></div>
  <div class="step" style="left:152px;top:516px"><h3>Organizing</h3><p>We plan dates, groups and rooms so that training fits your working week.</p></div>
</section>

<section class="testimonials">
  <h2 class="section-title">Client Testimonials</h2>
  <div class="title-rule"></div>
  <span class="slide-arrow" style="left:28px;top:256px"><svg width="10" height="14" viewBox="0 0 10 14"><path d="M8 1 2 7l6 6" fill="none" stroke="#888" stroke-width="2"/></svg></span>
  <span class="slide-arrow" style="left:1138px;top:256px"><svg width="10" height="14" viewBox="0 0 10 14"><path d="M2 1l6 6-6 6" fill="none" stroke="#888" stroke-width="2"/></svg></span>

  <div class="testimonial" style="left:108px">
    <span class="avatar" role="img" aria-label="Portrait photo of Lena Varga"></span>
    <span class="quote-mark">&ldquo;</span>
    <blockquote>The course was clear and practical. Our whole team now works faster with new digital tools.</blockquote>
    <span class="who">Lena Varga</span><span class="role">Financial Services Professional</span>
    <div class="stars"><svg width="96" height="16" viewBox="0 0 96 16" fill="#ffc214"><path id="s" d="M8 0l2.4 5 5.6.6-4.2 3.8 1.2 5.6L8 12.2 3 15l1.2-5.6L0 5.6 5.6 5z"/><use href="#s" x="20"/><use href="#s" x="40"/><use href="#s" x="60"/><use href="#s" x="80" fill="#ddd"/></svg></div>
  </div>
  <div class="testimonial" style="left:455px">
    <span class="avatar" role="img" aria-label="Portrait photo of Tomas Reyl"></span>
    <span class="quote-mark">&ldquo;</span>
    <blockquote>Trainers who know real projects. I used what I learned at work the very next morning.</blockquote>
    <span class="who">Tomas Reyl</span><span class="role">Program Lead, Civic Learning Centre</span>
    <div class="stars"><svg width="96" height="16" viewBox="0 0 96 16" fill="#ffc214"><use href="#s"/><use href="#s" x="20"/><use href="#s" x="40"/><use href="#s" x="60"/><use href="#s" x="80"/></svg></div>
  </div>
  <div class="testimonial" style="left:800px">
    <span class="avatar" role="img" aria-label="Portrait photo of Ines Harlow"></span>
    <span class="quote-mark">&ldquo;</span>
    <blockquote>A friendly, well organised program that helped our company plan its digital change with confidence.</blockquote>
    <span class="who">Ines Harlow</span><span class="role">Creative Strategist, Entrepreneur &amp; Consultant</span>
    <div class="stars"><svg width="96" height="16" viewBox="0 0 96 16" fill="#ffc214"><use href="#s"/><use href="#s" x="20"/><use href="#s" x="40"/><use href="#s" x="60"/><use href="#s" x="80" fill="#ddd"/></svg></div>
  </div>
</section>

<section class="clients">
  <h2 class="section-title">Our Clients</h2>
  <div class="title-rule"></div>
  <span class="client-arrow" style="left:68px">&lsaquo;</span>
  <span class="client-arrow" style="left:1116px">&rsaquo;</span>
  <div class="client-row">
    <div class="client" style="font-weight:400;color:#888">Company Logo</div>
    <div class="client">Brelvik Funds</div>
    <div class="client"><i></i>Oskelm</div>
    <div class="client">Tarvinne</div>
    <div class="client">Quillora</div>
    <div class="client" style="color:#999">Vantry Heat</div>
  </div>
</section>

<section class="contact">
  <h2 class="section-title">Contact Form</h2>
  <div class="title-rule"></div>
  <div class="field" style="left:145px;top:215px;width:447px">Name</div>
  <div class="field" style="left:604px;top:215px;width:451px">Email</div>
  <div class="field" style="left:145px;top:275px;width:447px">Phone</div>
  <div class="field" style="left:604px;top:275px;width:451px">Address</div>
  <div class="field" style="left:145px;top:335px;width:910px;height:110px">Message</div>
  <span class="btn">Submit message</span>
</section>

<footer class="site-footer">
  <div class="footer-brand abs"><span class="brand-mark"></span><span class="brand-name">Institute of Digital Craft</span></div>
  <div class="socials abs"><span></span><span></span><span></span><span></span></div>

  <div class="footer-col abs" style="left:452px;top:78px;width:260px">
    <h4>Contact Us</h4>
    <ul class="contact-list">
      <li><svg width="14" height="18" viewBox="0 0 14 18"><path d="M7 0a7 7 0 0 0-7 7c0 5 7 11 7 11s7-6 7-11a7 7 0 0 0-7-7zm0 10a3 3 0 1 1 0-6 3 3 0 0 1 0 6z" fill="#fff"/></svg><span>131 Quay Lane, Suite 4<br>Harbor Town, 10254</span></li>
      <li><svg width="14" height="16" viewBox="0 0 14 16"><path d="M3 0h3l1 4-2 1.5a9 9 0 0 0 3.5 3.5L10 7l4 1v3c0 1-1 2-2 2A12 12 0 0 1 1 2c0-1 1-2 2-2z" fill="#fff"/></svg><span>1 555 010 2040</span></li>
      <li><svg width="16" height="12" viewBox="0 0 16 12"><rect width="16" height="12" rx="1" fill="#fff"/><path d="M1 1l7 6 7-6" fill="none" stroke="#161616" stroke-width="1.5"/></svg><span>hello@digitalcraft.example</span></li>
    </ul>
  </div>
  <div class="footer-col abs" style="left:766px;top:78px">
    <h4>Quick Links</h4>
    <ul><li>Home</li><li>About us</li><li>Our Services</li><li>Blog</li><li>Contact</li></ul>
  </div>
  <div class="footer-col abs" style="left:948px;top:78px">
    <h4>Other Links</h4>
    <ul><li>FAQ</li><li>Support</li><li>Sitemap</li><li>Terms Of Use</li><li>Privacy Statement</li></ul>
  </div>
  <div class="copyright">&copy; copyright 2018 Institute of Digital Craft. All Rights Reserved</div>
</footer>

</body>
</html>
```